Reid Calloway Fitness Business Card

I Need a really cool and creative yet modern and cutting edge. I run a personal training company, I have a logo already which ill submit images of. Id like the base colors to be black and white with a little red as a highlight color. Charcoal grey is fine also. My clientele is mostly comprised of young professionals who are in touch with modern culture art and are interested in "cool" so if there was one thing i want this business card to be it sexy and cool.

Target Market(s)

young professionals who are image conscious, care about their health, looking and feeling good. They know what is cool and expect the best.

Industry/Entity Type

Training

Requirements
Must have
• - must be a 2 sided card
- must include the following:

Reid Calloway CPT
604 392 7715
Reid@ReidCallowayFitness.example
www.ReidCallowayFitness.example
Nice to have
• id like to see some unconventional shape ideas as well as conventional ones

```html
<!DOCTYPE html>
<html lang="en">
<head>
<meta charset="utf-8">
<title>Reid Calloway Fitness – Business Card</title>
<link rel="stylesheet" href="https://fonts.googleapis.com/css2?family=Questrial&display=swap">
<style>
  :root {
    --page-bg: #0c0c0c;
    --card-front: #1b1b1b;
    --card-back: #2a2a2a;
    --ink: #f2f2f2;
    --ink-soft: #cfcfcf;
    --accent: #e01b24;
  }
  * { margin: 0; padding: 0; box-sizing: border-box; }
  html, body {
    width: 1200px;
    height: 871px;
    overflow: hidden;
    background: var(--page-bg);
    font-family: "Questrial", "Helvetica Neue", Arial, sans-serif;
  }
  .stage {
    position: relative;
    width: 1200px;
    height: 871px;
  }
  .card {
    position: absolute;
    top: 281px;
    width: 540px;
    height: 309px;
    border-radius: 26px;
    overflow: hidden;
    box-shadow: 0 18px 40px rgba(0, 0, 0, 0.6);
  }
  .card--back { left: 40px; background: var(--card-back); }
  .card--front { left: 620px; background: var(--card-front); }

  /* Front */
  .front-lockup {
    position: absolute;
    left: 50%;
    top: 118px;
    transform: translateX(-50%);
    display: flex;
    flex-direction: column;
    align-items: flex-end;
    gap: 8px;
  }
  .front-mark {
    display: flex;
    align-items: center;
    gap: 12px;
    white-space: nowrap;
  }
  .front-mark__name {
    color: var(--ink);
    font-size: 30px;
    letter-spacing: 1px;
  }
  .mark-dot {
    width: 12px;
    height: 12px;
    border-radius: 50%;
    background: var(--accent);
    flex: none;
  }
  .tagline {
    font-size: 12px;
    color: var(--ink);
    white-space: nowrap;
  }
  .tagline__lead { color: var(--accent); }

  /* Back */
  .back-mark {
    position: absolute;
    left: 30px;
    top: 38px;
    display: flex;
    align-items: center;
    gap: 8px;
    color: var(--ink);
    font-size: 18px;
    white-space: nowrap;
  }
  .back-mark .mark-dot { width: 8px; height: 8px; }
  .rule {
    position: absolute;
    height: 2px;
    background: var(--accent);
  }
  .rule--contact-top { left: 250px; right: 0; top: 112px; }
  .rule--contact-bottom { left: 250px; right: 0; top: 196px; }
  .rule--name-top { left: 0; width: 230px; top: 150px; }
  .rule--name-bottom { left: 0; width: 230px; top: 246px; }
  .contact {
    position: absolute;
    left: 262px;
    top: 124px;
    list-style: none;
    color: var(--ink-soft);
    font-size: 14px;
    line-height: 22px;
    white-space: nowrap;
  }
  .person {
    position: absolute;
    left: 30px;
    top: 168px;
    color: var(--ink-soft);
  }
  .person__name, .person__title { font-size: 20px; line-height: 28px; }
</style>
</head>
<body>
<main class="stage">
  <section class="card card--back" aria-label="Card back">
    <div class="back-mark"><span class="mark-dot"></span><span>Reid Calloway Fitness</span></div>
    <div class="rule rule--contact-top"></div>
    <ul class="contact">
      <li>604 392 7715</li>
      <li>Reid@ReidCallowayFitness.example</li>
      <li>www.ReidCallowayFitness.example</li>
    </ul>
    <div class="rule rule--contact-bottom"></div>
    <div class="rule rule--name-top"></div>
    <div class="person">
      <p class="person__name">Reid Calloway</p>
      <p class="person__title">CPT</p>
    </div>
    <div class="rule rule--name-bottom"></div>
  </section>

  <section class="card card--front" aria-label="Card front">
    <div class="front-lockup">
      <div class="front-mark">
        <span class="front-mark__name">Reid Calloway Fitness</span>
        <span class="mark-dot"></span>
      </div>
      <p class="tagline"><span class="tagline__lead">Move</span>...Forward</p>
    </div>
  </section>
</main>
</body>
</html>
```